IRON SASH VIGOUR CERTIFICATE

Carrowby Hapkido Inc is wanting to introduce a fitness system based upon certificates reflecting rank; White - Yellow - Blue - Red - Black.

The Certificate "MUST" have on it "IRON SASH VIGOUR"

The Certificate "MUST" have a martial arts theme!

The Certificate "MUST" reflect the fitness requirements for each rank.

The colour scheme for each Certificate "MUST" reflect the belt rank

The Certificate must include at least one martial arts graphic / motif

The certificate must have the Carrowby HKD LOGO

We will need a certificate template that can be for all levels but reflect the rank and fitness level. The certificate can be either traditional or modern style but must reflect a martial art themes. The certificate must have the Carrowby Hapkido logo incorporated into the certificate with signature space for senior instructors Dan Pellow & Sorna Vick-Pellow. The certificates should be eye catching and exciting to look at. It should bold and incorporate martial art motifs etc The fitness requirements are not onerous and the certificate system is created to incentivise physical activity and correct technique rather than creating an impossible standards only Olympians can achieve. The majority of our students are upper primary and lower secondary from 11yr-15yrs. Certificate should be youthful but not silly. The certificate template will be reproduced for each colour belt.White = 10 push ups 10 Sit ups 10 squats 10 Jumping Jacks 20 sec plank 400m continuous run Demonstrate beginner stretching techniqueYellow = 20 push ups 20 sit ups 20 squats 20 Jumping Jacks 40 Sec plank 800m continuous run Demonstrate intermediate stretching techniqueBlue = 30 push ups 30 sit ups 30 squats 30 Jumping Jacks 60 Sec plank 1200m continuous run Demonstrate intermediate stretching techniqueRed = 40 push ups 40 sit ups 40 squats 40 Jumping Jacks 75sec plank 1600m run Demonstrate advanced stretching techniqueBlack = 50 push ups 50 sit ups 50 squats 50 Jumping jacks 90 sec planks 2000m continuous run Demonstrate advanced stretching technique
Updates

HI Designers, Please go for modern and professionals. Several designs have used traditional motifs of water dragons or lattice bordering. This looks old school. Please do not use martial art silhouettes as it looks amateur. Definately looking for upmarket high quality presentations.

Logo Text

IRON SASH VIGOUR

Font styles to use
Decorative

Colors

Designer to choose colors to be used in the design.

Requirements
Must have
• This will be a template foe all coloured ranks of fitness, Be bold, memorable, should be themed to martial arts etc

```html
<!DOCTYPE html>
<html lang="en">
<head>
<meta charset="utf-8">
<title>Certificate of Completion – Carrowby Hapkido</title>
<link href="https://fonts.googleapis.com/css2?family=Cinzel:wght@400;600;700&family=Great+Vibes&family=Open+Sans:wght@400;600&display=swap" rel="stylesheet">
<style>
  :root {
    --page-bg: #d6d6d6;
    --paper: #ffffff;
    --navy: #262d40;
    --red: #e3202a;
    --rule: #3a3f4c;
    --muted-line: #8c7f78;
  }
  * { margin: 0; padding: 0; box-sizing: border-box; }
  html, body { width: 1200px; height: 1120px; overflow: hidden; }
  body { background: var(--page-bg); position: relative; font-family: "Open Sans", sans-serif; }

  .certificate {
    position: absolute; left: 40px; top: 160px;
    width: 1120px; height: 800px;
    background: var(--paper);
    box-shadow: 0 6px 22px rgba(0,0,0,.18);
  }
  .border-ornament {
    position: absolute; inset: 14px;
    border: 34px solid transparent;
    border-image: linear-gradient(135deg, #a3a7b2, #6e7382, #a3a7b2) 1;
    outline: 2px solid var(--rule); outline-offset: -2px;
  }
  .inner-frame {
    position: absolute; inset: 62px;
    border: 2px solid var(--rule);
  }
  .inner-frame::after {
    content: ""; position: absolute; inset: 5px;
    border: 1px solid var(--rule);
  }

  .rank-ribbon { position: absolute; left: 116px; top: 64px; width: 62px; height: 290px; }
  .rank-label {
    position: absolute; left: 116px; top: 305px; width: 62px;
    text-align: center; font-family: "Cinzel", serif; font-size: 11px; color: #fff; letter-spacing: .5px;
  }
  .belt-art {
    position: absolute; left: 72px; top: 160px; width: 148px; height: 96px;
    background: linear-gradient(160deg, #353c52, var(--navy));
    border-radius: 50% 50% 34% 34%;
  }

  .club-ribbon { position: absolute; left: 900px; top: 64px; width: 62px; height: 270px; }
  .club-mark {
    position: absolute; left: 855px; top: 100px; width: 152px; height: 152px;
    border-radius: 50%; background: var(--navy);
    display: flex; align-items: center; justify-content: center; text-align: center;
    font-family: "Cinzel", serif; font-weight: 700; font-size: 17px; line-height: 1.25; color: #fff;
  }

  .flourish {
    position: absolute; left: 460px; top: 92px; width: 170px; height: 40px;
    background: radial-gradient(ellipse at center, rgba(227,32,42,.55), rgba(227,32,42,0) 70%);
  }

  .title {
    position: absolute; left: 230px; width: 620px; top: 136px; text-align: center;
    font-family: "Cinzel", serif; font-weight: 700; font-size: 70px; line-height: 1; color: var(--navy); letter-spacing: 1px;
    white-space: nowrap;
  }
  .subtitle-row {
    position: absolute; left: 230px; width: 620px; top: 218px;
    display: flex; align-items: center; justify-content: center; gap: 14px;
  }
  .subtitle-row .swash { width: 120px; height: 2px; background: var(--red); }
  .subtitle {
    font-family: "Cinzel", serif; font-size: 18px; color: var(--navy); letter-spacing: 2px;
  }
  .presented {
    position: absolute; left: 0; right: 0; top: 284px; text-align: center;
    font-family: "Cinzel", serif; font-size: 20px; color: var(--red); letter-spacing: 1px;
  }
  .recipient {
    position: absolute; left: 0; right: 0; top: 330px; text-align: center;
    font-family: "Great Vibes", cursive; font-size: 74px; line-height: 1.2; color: var(--red);
  }
  .recipient-rule { position: absolute; left: 370px; width: 390px; top: 438px; height: 2px; background: var(--rule); }
  .rank-name {
    position: absolute; left: 0; right: 0; top: 450px; text-align: center;
    font-family: "Cinzel", serif; font-size: 15px; color: var(--navy); letter-spacing: 1px;
  }
  .requirements {
    position: absolute; left: 0; right: 0; top: 476px; text-align: center;
    font-size: 13px; line-height: 1.35; color: var(--navy);
  }
  .program-name {
    position: absolute; left: 0; right: 0; top: 534px; text-align: center;
    font-family: "Cinzel", serif; font-weight: 700; font-size: 18px; letter-spacing: 4px; color: var(--red);
  }

  .sign-field { position: absolute; font-size: 13px; color: var(--navy); }
  .sign-field .line { height: 1px; background: var(--muted-line); margin-bottom: 8px; }
  .sign-field.signature { left: 730px; top: 600px; width: 240px; text-align: center; }
  .sign-field.date { left: 190px; top: 660px; width: 240px; }
  .sign-field.date span { margin-left: 90px; }
</style>
</head>
<body>
  <main class="certificate">
    <div class="border-ornament" role="img" aria-label="Ornamental scrollwork border"></div>
    <div class="inner-frame"></div>

    <svg class="rank-ribbon" viewBox="0 0 62 290" aria-hidden="true">
      <polygon points="0,0 62,0 62,290 31,272 0,290" fill="var(--red)"/>
    </svg>
    <div class="belt-art" role="img" aria-label="Tied martial arts belt illustration"></div>
    <div class="rank-label">YELLOW</div>

    <svg class="club-ribbon" viewBox="0 0 62 270" aria-hidden="true">
      <polygon points="0,0 62,0 62,270 31,252 0,270" fill="var(--red)"/>
    </svg>
    <div class="club-mark">CARROWBY<br>HAPKIDO</div>

    <div class="flourish" role="img" aria-label="Red calligraphic flourish ornament"></div>

    <h1 class="title">CERTIFICATE</h1>
    <div class="subtitle-row">
      <span class="swash"></span>
      <span class="subtitle">OF COMPLETION</span>
      <span class="swash"></span>
    </div>
    <p class="presented">THIS CERTIFICATE IS PROUDLY PRESENTED TO</p>
    <p class="recipient">Name Here</p>
    <div class="recipient-rule"></div>
    <p class="rank-name">WHITE BELT</p>
    <p class="requirements">10 push ups 10 Sit ups 10 squats 10 Jumping Jacks 20 sec plank 400m<br>continuous run Demonstrate beginner stretching technique</p>
    <p class="program-name">IRON SASH VIGOUR</p>

    <div class="sign-field signature"><div class="line"></div>SIGNATURE</div>
    <div class="sign-field date"><div class="line"></div><span>DATE</span></div>
  </main>
</body>
</html>
```